Bright Ledger Path LLC Seminar Workbook Template

Our mission: Our mission is to provide students with amazing accounting literacy experiences in amazing learning environments so they can accomplish amazing career and business goals.
We would like to have a Microsoft Word template that we can use for all of our course content. We are profession; yet not stuffy. We teach a timeless subject; yet we are very modern.
Our logo is attached. We would like our logo or parts of our logo to be incorporated into the template (for example, perhaps the tagline is included in the bottom right corner). We have also attached a sample of a company's work. We do not like their design; but it's the kind of end product that we are interested in.
We are grateful for anyone who is interested in this project. Thank you for your help.

```html
<!DOCTYPE html>
<html lang="en">
<head>
<meta charset="UTF-8">
<title>Bright Ledger Path LLC – Course Creation Starter Kit</title>
<link rel="stylesheet" href="https://fonts.googleapis.com/css2?family=Poppins:ital,wght@0,400;0,500;0,700;0,800;1,400&display=swap">
<style>
  :root {
    --paper: #f4f4f4;
    --ink: #1c1c1c;
    --green: #7dbb3c;
    --blue: #0f9ad9;
    --red: #e3231b;
    --gold: #f2a81d;
    --check: #5aa646;
  }
  * { box-sizing: border-box; margin: 0; padding: 0; }
  html, body { width: 1070px; height: 1200px; overflow: hidden; }
  body {
    background: var(--paper);
    font-family: "Poppins", sans-serif;
    color: var(--ink);
    position: relative;
  }
  .page { position: relative; width: 1070px; height: 1200px; overflow: hidden; }

  .accent-bar {
    position: absolute; left: 52px; top: 0;
    width: 106px; height: 674px;
    background: var(--green);
  }
  .title {
    position: absolute; left: 50px; top: 205px;
    font-weight: 800; font-size: 55px; line-height: 55px;
    letter-spacing: -0.5px;
    color: #111;
  }
  .pointer-arrows {
    position: absolute; left: 183px; top: 531px;
    width: 48px; height: 122px;
  }

  .brand {
    position: absolute; left: 383px; top: 112px; width: 586px;
    display: flex; align-items: center; justify-content: center; gap: 14px;
  }
  .brand-dot { width: 18px; height: 18px; border-radius: 50%; background: var(--green); }
  .brand-name { font-weight: 500; font-size: 34px; color: var(--blue); letter-spacing: -0.3px; }

  .intro {
    position: absolute; left: 383px; top: 226px; width: 590px;
    font-size: 16.2px; line-height: 23.3px; letter-spacing: -0.2px;
  }
  .intro p { margin-bottom: 11px; }
  .intro strong { font-weight: 700; }
  .intro .aside { font-style: italic; }

  .section-heading {
    position: absolute; left: 48px; top: 732px;
    font-weight: 700; font-size: 37px; line-height: 40px;
    letter-spacing: -0.4px;
  }
  .section-lead {
    position: absolute; left: 49px; top: 940px; width: 300px;
    font-size: 16.2px; line-height: 23px; letter-spacing: -0.2px;
  }

  .decorative-circle {
    position: absolute; left: 905px; top: 807px;
    width: 272px; height: 272px; border-radius: 50%;
    background: var(--blue);
  }

  .decision { position: absolute; left: 386px; width: 560px; }
  .decision-label {
    font-weight: 700; font-size: 26px; line-height: 30px;
    letter-spacing: 0.3px; margin-bottom: 10px;
  }
  .decision-1 { top: 736px; }
  .decision-1 .decision-label { color: var(--red); }
  .decision-2 { top: 912px; }
  .decision-2 .decision-label { color: var(--blue); }
  .decision-3 { top: 1010px; }
  .decision-3 .decision-label { color: var(--gold); }

  .question {
    list-style: none;
    position: relative;
    padding-left: 44px; margin-bottom: 11px;
    font-weight: 700; font-size: 16.4px; line-height: 23.5px;
    letter-spacing: -0.2px;
  }
  .question svg { position: absolute; left: 22px; top: 3px; width: 17px; height: 17px; }
  .question em { font-weight: 400; }
</style>
</head>
<body>
<main class="page">
  <div class="accent-bar"></div>
  <h1 class="title">The<br>ultimate<br>course<br>creation<br>starter<br>kit</h1>
  <svg class="pointer-arrows" viewBox="0 0 48 122" aria-hidden="true">
    <polygon points="2,0 46,0 24,34" fill="#0f9ad9"/>
    <polygon points="2,44 46,44 24,78" fill="#0f9ad9"/>
    <polygon points="2,88 46,88 24,122" fill="#0f9ad9"/>
  </svg>

  <div class="brand">
    <span class="brand-dot"></span>
    <span class="brand-name">Bright Ledger Path LLC</span>
  </div>

  <section class="intro">
    <p>Imagine how it will feel when you create a profitable digital course in your business. One that you can promote over and over again this year and beyond.</p>
    <p>Not only will you get to share your knowledge and expertise with hundreds or even thousands of students all over the world, but you’ll be able to do so with less stress and fewer skipped family meals than your current situation demands of you.</p>
    <p>Instead, you’ll be able to sit with your family and proudly share the fact that someone in Australia, or Singapore, or Brazil just took your course and improved their life for the better.</p>
    <p><strong>Can you even imagine that?</strong> Now that’s “next level” cool.</p>
    <p>With a profitable digital course, you’ll also get to officially escape the time-for-money trap, and you’ll have the freedom to say “no” to opportunities or clients that don’t feel 100% aligned with who you are and the life you want to live.</p>
    <p class="aside">(Oftentimes what you say “no” to is just as important as the things you say “yes” to in your business)</p>
  </section>

  <h2 class="section-heading">Getting<br>started with<br>your digital<br>course</h2>
  <p class="section-lead">To help you kickstart your digital course journey, there are three important decisions you need to make. The good news? Once you have all the details (which I’m going to give you in the starter kit) they are pretty easy decisions to make!</p>

  <div class="decorative-circle"></div>

  <section class="decision decision-1">
    <h3 class="decision-label">DECISION 1</h3>
    <ul>
      <li class="question"><svg viewBox="0 0 20 20" aria-hidden="true"><circle cx="10" cy="10" r="10" fill="#5aa646"/><path d="M5.5 10.3l3 3 6-6.2" stroke="#fff" stroke-width="2.2" fill="none" stroke-linecap="round" stroke-linejoin="round"/></svg>What will your course be about?</li>
      <li class="question"><svg viewBox="0 0 20 20" aria-hidden="true"><circle cx="10" cy="10" r="10" fill="#5aa646"/><path d="M5.5 10.3l3 3 6-6.2" stroke="#fff" stroke-width="2.2" fill="none" stroke-linecap="round" stroke-linejoin="round"/></svg>What topics will spark the most interest and engagement from your community so that they will be eager to buy?</li>
    </ul>
  </section>

  <section class="decision decision-2">
    <h3 class="decision-label">DECISION 2</h3>
    <ul>
      <li class="question"><svg viewBox="0 0 20 20" aria-hidden="true"><circle cx="10" cy="10" r="10" fill="#5aa646"/><path d="M5.5 10.3l3 3 6-6.2" stroke="#fff" stroke-width="2.2" fill="none" stroke-linecap="round" stroke-linejoin="round"/></svg>What are you going to name your course?</li>
    </ul>
  </section>

  <section class="decision decision-3">
    <h3 class="decision-label">DECISION 3</h3>
    <ul>
      <li class="question"><svg viewBox="0 0 20 20" aria-hidden="true"><circle cx="10" cy="10" r="10" fill="#5aa646"/><path d="M5.5 10.3l3 3 6-6.2" stroke="#fff" stroke-width="2.2" fill="none" stroke-linecap="round" stroke-linejoin="round"/></svg>What are you going to stop doing in your business once you’re generating revenue with your digital course? <em>(This one is an extra fun to explore, so we will keep it for the final decision)</em></li>
    </ul>
  </section>
</main>
</body>
</html>
```